Business card for utility of the future

I need a business card template designed for brookvane. We provide sustainable water, energy and waste services to homes.

The card should include name, position, email address, phone number, website and our logo (attached). I would like it to convey professionalism and creativity.

Target Market(s)

Homeowners, investors, corporate partners.

Industry/Entity Type

Utility

Contact Information for Business Card

The card should include name, position, email address, phone number, website and our logo (attached).

```html
<!DOCTYPE html>
<html lang="en">
<head>
<meta charset="utf-8">
<title>brookvane business card</title>
<link rel="stylesheet" href="https://fonts.googleapis.com/css2?family=Open+Sans:wght@400;600;700;800&display=swap">
<style>
  :root {
    --stage: #e8e5e0;
    --paper: #ffffff;
    --leaf: #6dbf85;
    --coral: #f08a5d;
    --shadow: rgba(0, 0, 0, 0.18);
  }
  * { box-sizing: border-box; margin: 0; padding: 0; }
  html, body {
    width: 1200px; height: 1000px; overflow: hidden;
    background: var(--stage);
    font-family: "Open Sans", Arial, sans-serif;
  }
  .card {
    position: absolute; left: 266px; width: 666px; height: 397px;
    border-radius: 24px; overflow: hidden;
    box-shadow: 0 6px 14px var(--shadow);
  }
  .card--front { top: 74px; background: var(--paper); }
  .card--back { top: 533px; background: var(--leaf); }

  .front-wave { position: absolute; inset: 0; width: 666px; height: 397px; }

  .wordmark {
    position: absolute; font-weight: 700; letter-spacing: -1.5px; line-height: 1;
    white-space: nowrap;
  }
  .card--front .wordmark { left: 32px; top: 74px; font-size: 56px; color: var(--leaf); }
  .card--back .wordmark {
    left: 50%; top: 52%; transform: translate(-50%, -50%);
    font-size: 76px; color: var(--paper);
  }

  .person { position: absolute; right: 34px; top: 76px; text-align: right; }
  .person__name { font-size: 24px; font-weight: 700; color: var(--leaf); letter-spacing: 0.5px; line-height: 1.15; }
  .person__role { font-size: 20px; color: var(--coral); line-height: 1.2; }

  .address {
    position: absolute; right: 34px; top: 212px; text-align: right;
    color: var(--paper); font-size: 17px; line-height: 24px;
  }
  .contacts {
    position: absolute; right: 32px; top: 272px; list-style: none;
    color: var(--paper); font-size: 17px; line-height: 25px;
  }
  .contacts li { display: flex; justify-content: flex-end; align-items: center; gap: 6px; }
  .contacts svg { width: 16px; height: 16px; fill: var(--paper); flex: none; }

  .tagline {
    position: absolute; left: 32px; top: 330px; width: 320px;
    color: var(--paper); font-size: 17px; line-height: 21px;
  }
</style>
</head>
<body>
  <section class="card card--front">
    <svg class="front-wave" viewBox="0 0 666 397" aria-hidden="true">
      <path fill="#6dbf85" d="M0,296 C150,336 260,318 360,248 C450,184 560,156 666,166 L666,397 L0,397 Z"/>
    </svg>

    <div class="wordmark">brookvane</div>

    <div class="person">
      <p class="person__name">JONAS ARVID</p>
      <p class="person__role">Founder</p>
    </div>

    <p class="address">482 Alder Creek Rd,<br>Fenwick, MD 21390</p>

    <ul class="contacts">
      <li>+ 000 000 0000
        <svg viewBox="0 0 16 16"><path d="M2 6c0-2 3-3 6-3s6 1 6 3v1h-3V6H5v1H2z M4 8h8l1 5H3z"/></svg></li>
      <li>+ 000 000 0000
        <svg viewBox="0 0 16 16"><path d="M4 2h8v3H4z M2 6h12v6h-2v-2H4v2H2z M5 11h6v3H5z"/></svg></li>
      <li>info@brookvane.com
        <svg viewBox="0 0 16 16"><path d="M1 4h14v1l-7 4-7-4z M1 6.5l7 4 7-4V13H1z"/></svg></li>
      <li>www.brookvane.com
        <svg viewBox="0 0 16 16"><path d="M8 1a7 7 0 1 0 0 14A7 7 0 0 0 8 1zm0 2a5 5 0 0 1 4.6 3H10V4.4A5 5 0 0 0 8 3zM3.4 6H6v4H3.4a5 5 0 0 1 0-4zM8 13a5 5 0 0 1-4.6-3H6v2.6c.6.3 1.3.4 2 .4zm1-5 6 3-2.5 1 2 2-1 1-2-2L10 15z"/></svg></li>
    </ul>

    <p class="tagline">provide sustainable water, energy and waste services to homes.</p>
  </section>

  <section class="card card--back">
    <div class="wordmark">brookvane</div>
  </section>
</body>
</html>
```